Design WORDPRESS Website for E Commerce Business

We are needing a WORDPRESS website for an E Commerce Business that is supplying quailty kids / baby products.

Target Market(s)

Female / Working Mums / New Mums

Industry/Entity Type

Business

Number of Pages Required

1 page

Font styles to use
Sans Serif

Colors
33b8a4
f8fcfd
d3a5cc
f7f1f7
cbcbcb
9d9d9d

```html
<!DOCTYPE html>
<html lang="en">
<head>
<meta charset="utf-8">
<title>Pip &amp; Pod — Kids Store</title>
<link href="https://fonts.googleapis.com/css2?family=Montserrat:ital,wght@0,400;0,600;0,700;1,700&family=Open+Sans:wght@400;600&display=swap" rel="stylesheet">
<style>
:root{
  --bg:#f0f0f0;
  --pink:#f2a7c4;
  --pink-soft:#f4b8cd;
  --lilac:#c8b3f2;
  --lilac-soft:#e2c7f0;
  --sky:#bcd0ea;
  --blue:#6a7ed8;
  --teal:#7fd0c4;
  --sun:#fdd283;
  --text:#6e6e6e;
  --muted:#9d9d9d;
  --white:#fff;
  --sage:#dfe3dc;
  --magenta:#f29ee3;
  --footer:#a9c0e4;
  --footer-bar:#8ca3d2;
  --orange:#f6b06e;
}
*{box-sizing:border-box;margin:0;padding:0}
html,body{width:1200px;height:3854px;overflow:hidden}
body{background:var(--bg);font-family:"Open Sans",Arial,sans-serif;color:var(--text);position:relative}
.abs{position:absolute}
.head{font-family:"Montserrat",Arial,sans-serif}

.logo{left:115px;top:28px;display:flex;align-items:center;gap:12px}
.logo-dot{width:44px;height:44px;border-radius:50%;background:var(--muted)}
.logo-name{font-family:"Montserrat",Arial,sans-serif;font-weight:700;font-size:24px;color:var(--teal);line-height:1}
.search{left:320px;top:38px;width:270px;height:34px;border-radius:17px;background:#e3e3e3;display:flex;align-items:center;padding-left:18px;font-size:14px;color:#b5b5b5}
.search-btn{position:absolute;right:2px;top:2px;width:30px;height:30px;border-radius:50%;background:var(--blue)}
.util{top:44px;font-size:14px;color:var(--muted)}
.cart{left:955px;top:44px;font-size:14px;color:var(--muted)}
.cart b{color:var(--blue);font-weight:600}

.nav{left:0;top:105px;width:1200px;height:70px;background:var(--pink-soft);display:flex;align-items:center}
.nav-menu{position:absolute;left:130px;top:26px;width:22px;height:16px;border-top:3px solid #fff;border-bottom:3px solid #fff}
.nav-menu:after{content:"";position:absolute;left:0;top:4px;width:22px;height:3px;background:#fff}
.nav ul{list-style:none;display:flex;gap:36px;margin-left:215px;font-family:"Montserrat",Arial,sans-serif;font-size:15px;letter-spacing:3px;color:#fff;font-weight:600}

.hero-kicker{left:280px;top:364px;font-size:12px;letter-spacing:3px;color:var(--orange);font-weight:600}
.hero-title{left:280px;top:396px;font-size:40px;letter-spacing:10px;line-height:47px;font-weight:700;color:var(--muted)}
.hero-title .t{color:var(--teal)}
.hero-title .b{color:var(--blue)}
.btn{display:inline-flex;align-items:center;background:var(--pink);color:#fff;font-size:13px;letter-spacing:2px;border-radius:6px;padding:0 18px;height:42px;font-family:"Montserrat",Arial,sans-serif}
.hero-photo{left:730px;top:228px;width:170px;height:462px;border-radius:70px 70px 20px 20px;background:linear-gradient(#f3a9cf,#9bb3e0 55%,#8f9cae)}

.promo-frame{position:absolute;border:3px dashed #fff}
.promo-title{font-size:26px;letter-spacing:6px;color:#fff;font-weight:700;text-align:center;line-height:34px}
.promo-small{font-size:11px;letter-spacing:2px;color:#fff;font-weight:600}
.photo{border-radius:4px}

.coll{left:170px;top:1190px;width:860px;height:585px;background:#f4ecee}
.sec-title{font-family:"Montserrat",Arial,sans-serif;font-weight:700;letter-spacing:5px;color:var(--blue);font-size:27px;text-align:center;width:100%}
.tabs{top:1293px;left:360px;display:flex;gap:30px;font-family:"Montserrat",Arial,sans-serif;font-size:17px;letter-spacing:2px;color:var(--blue);font-weight:600}
.tabs .on{background:#f6c6a8;color:#fff;border-radius:6px;padding:0 12px}
.arrow{width:26px;height:26px;top:1330px;border-radius:3px}
.card-img{width:238px;height:345px;background:linear-gradient(#e8e3e4,#d9d3d5)}
.card-name{font-size:12px;letter-spacing:3px;color:var(--muted);text-align:center;width:238px;font-weight:600}
.card-price{font-size:19px;letter-spacing:3px;color:var(--text);text-align:center;width:238px;font-family:"Montserrat",Arial,sans-serif;font-weight:600}
.side-btn{width:34px;height:34px;background:var(--pink);border-radius:4px}

.deal-left{left:110px;top:1833px;width:493px;height:502px;background:var(--sage)}
.deal-right{left:603px;top:1833px;width:492px;height:502px;background:var(--magenta)}
.timer{width:70px;height:70px;border-radius:50%;background:#d98be6;color:#fff;text-align:center;font-family:"Montserrat",Arial,sans-serif;font-weight:700;font-size:26px;line-height:1;padding-top:14px}
.timer small{display:block;font-size:11px;font-weight:600;letter-spacing:1px;margin-top:2px}
.badge{width:112px;height:112px;border-radius:50%;background:#f3f0ea;left:544px}

.post-title{font-family:"Montserrat",Arial,sans-serif;font-weight:700;font-size:17px;letter-spacing:3px;color:var(--teal)}
.post-text{font-size:14px;line-height:23px;letter-spacing:1px;color:var(--text);width:410px}
.post-meta{font-size:13px;color:var(--muted);display:flex;gap:24px;align-items:center}
.post-meta .more{color:var(--pink)}

.news{left:250px;top:3245px;width:700px;height:135px;background:var(--blue);opacity:.85}
.news-frame{left:262px;top:3257px;width:676px;height:111px;border:2px solid rgba(255,255,255,.6)}

.footer{left:0;top:3455px;width:1200px;height:340px;background:var(--footer)}
.foot-h{font-family:"Montserrat",Arial,sans-serif;font-weight:700;font-size:19px;letter-spacing:4px;color:var(--sun)}
.foot-list{font-size:13px;line-height:21px;letter-spacing:1.5px;color:#fff;list-style:none}
.social{width:40px;height:40px;border-radius:50%;border:2px solid #fff}
.card-pay{width:44px;height:28px;border-radius:4px;background:#fff;opacity:.8}
.foot-bar{left:0;top:3795px;width:1200px;height:59px;background:var(--footer-bar);color:#fff;font-size:13px;letter-spacing:1px}
</style>
</head>
<body>

<div class="abs logo"><span class="logo-dot"></span><span class="logo-name">PIP<br>&amp; POD</span></div>
<div class="abs search">Search..<span class="search-btn"></span></div>
<div class="abs util" style="left:628px">My account ▾</div>
<div class="abs util" style="left:742px">Language ▾</div>
<div class="abs util" style="left:838px">Currency ▾</div>
<div class="abs cart">0 item(s) <b>$0.00</b></div>

<nav class="abs nav">
  <span class="nav-menu"></span>
  <ul><li>HOME</li><li>CATEGORIES ▾</li><li>BOYS ▾</li><li>GIRLS ▾</li><li>DEALS ▾</li><li>BLOG</li><li>CONTACT</li></ul>
</nav>

<svg class="abs" style="left:110px;top:175px" width="170" height="160" viewBox="0 0 170 160">
  <path d="M0 0H170A170 160 0 0 1 0 160Z" fill="var(--sun)"/>
</svg>
<svg class="abs" style="left:590px;top:480px" width="496" height="222" viewBox="0 0 496 222">
  <path d="M0 222A248 222 0 0 1 496 222Z" fill="var(--sun)"/>
</svg>
<div class="abs photo hero-photo" role="img" aria-label="Photo of a girl in a pink cap, denim jacket and skirt with pink leggings and boots"></div>

<div class="abs hero-kicker head">ONLINE SHOPPING STORE</div>
<div class="abs hero-title head">OUR KIDS<br><span class="t">JACKET</span><br>FASHION<br>IN <span class="b">STORE</span></div>
<div class="abs" style="left:280px;top:603px"><span class="btn">SHOP NOW</span></div>

<div class="abs" style="left:170px;top:727px;width:362px;height:411px;background:var(--lilac)"></div>
<div class="abs promo-frame" style="left:187px;top:744px;width:328px;height:377px"></div>
<div class="abs photo" style="left:175px;top:745px;width:140px;height:390px;background:linear-gradient(#e9d3c6,#5c7fae 55%,#9c7b5a)" role="img" aria-label="Photo of a girl in a white top and denim shorts"></div>
<div class="abs promo-small" style="left:320px;top:796px">ONLINE SHOPPING STORE</div>
<div class="abs promo-title head" style="left:320px;top:830px;width:200px">BIG<br>SALE</div>
<div class="abs promo-small" style="left:335px;top:928px;text-align:center;width:170px;line-height:18px">FROM 28 AUG - TILL<br>10 SEPTEMBER</div>
<div class="abs head" style="left:320px;top:966px;width:200px;text-align:center;color:#fff;font-weight:700;font-size:18px;letter-spacing:2px">-20% OFF</div>
<div class="abs" style="left:335px;top:1025px"><span class="btn" style="height:36px">SHOP NOW</span></div>

<div class="abs" style="left:588px;top:727px;width:442px;height:193px;background:var(--lilac-soft)"></div>
<div class="abs promo-frame" style="left:600px;top:739px;width:418px;height:169px"></div>
<div class="abs photo" style="left:605px;top:735px;width:120px;height:180px;background:linear-gradient(#a7c3e6,#f0df3b)" role="img" aria-label="Photo of a boy riding a yellow toy car"></div>
<div class="abs head" style="left:754px;top:757px;color:#fff;font-size:17px;font-weight:700;letter-spacing:4px">NEW COLLECTION</div>
<div class="abs promo-small" style="left:754px;top:787px;line-height:17px;font-weight:400">WE GOT THE SUMMER<br>COLLECTION FOR KIDS</div>
<div class="abs" style="left:754px;top:853px"><span class="btn" style="height:36px;background:#a99ee6">SHOP NOW</span></div>

<div class="abs" style="left:588px;top:945px;width:442px;height:193px;background:var(--sky)"></div>
<div class="abs promo-frame" style="left:600px;top:957px;width:418px;height:169px"></div>
<div class="abs photo" style="left:870px;top:960px;width:150px;height:175px;background:linear-gradient(#d4dce9,#4f6fb0)" role="img" aria-label="Photo of a toddler playing with toy blocks"></div>
<div class="abs head" style="left:624px;top:975px;color:#fff;font-size:17px;font-weight:700;letter-spacing:3px">ACCESORIES AND TOYS</div>
<div class="abs promo-small" style="left:624px;top:1005px;line-height:17px;font-weight:400">THE LAST ACCESORIES<br>FOR YOUR CHILDRENS</div>
<div class="abs" style="left:624px;top:1070px"><span class="btn" style="height:36px;background:#e7a2d6">SHOP NOW</span></div>

<div class="abs coll"></div>
<div class="abs sec-title" style="left:0;top:1230px">NEW COLLECTION</div>
<div class="abs tabs"><span class="on">Sale</span><span>Featured</span><span>Bestseller</span><span>Special</span></div>
<div class="abs arrow" style="left:948px;background:var(--pink)"></div>
<div class="abs arrow" style="left:985px;background:#bbb"></div>

<div class="abs card-img" style="left:183px;top:1370px;box-shadow:0 8px 14px rgba(0,0,0,.18)" role="img" aria-label="Photo of a jumping boy in a blue t-shirt and jeans"></div>
<div class="abs head" style="left:183px;top:1478px;height:34px;padding:0 12px;line-height:34px;background:var(--pink);color:#fff;font-size:11px;letter-spacing:2px">ADD PRODUCT</div>
<div class="abs side-btn" style="left:183px;top:1528px"></div>
<div class="abs side-btn" style="left:183px;top:1578px"></div>
<div class="abs card-img" style="left:485px;top:1370px" role="img" aria-label="Photo of a jumping girl in a pink top and purple leggings"></div>
<div class="abs card-img" style="left:783px;top:1370px" role="img" aria-label="Photo of a jumping girl in a purple top and green skirt"></div>
<div class="abs card-name" style="left:183px;top:1728px">PRODUCT NAME</div>
<div class="abs card-price" style="left:183px;top:1748px">$0.00</div>
<div class="abs card-name" style="left:485px;top:1728px">PRODUCT NAME</div>
<div class="abs card-price" style="left:485px;top:1748px">$0.00</div>
<div class="abs card-name" style="left:783px;top:1728px">PRODUCT NAME</div>
<div class="abs card-price" style="left:783px;top:1748px">$0.00</div>

<div class="abs deal-left"></div>
<div class="abs deal-right"></div>
<div class="abs" style="left:155px;top:1855px;width:275px;height:450px;border:3px dashed #fff"></div>
<div class="abs head" style="left:155px;top:1917px;width:275px;text-align:center;font-size:14px;letter-spacing:3px;font-weight:700;color:var(--text)">DEAL OF THE WEEK</div>
<div class="abs head" style="left:155px;top:1972px;width:275px;text-align:center;font-size:36px;letter-spacing:5px;font-weight:700;color:var(--muted);line-height:45px">UP TO 25%<br>OFF</div>
<div class="abs" style="left:185px;top:2085px;width:215px;text-align:center;font-size:12px;line-height:20px;letter-spacing:1px;color:var(--muted)">Lorem ipsum dolor sit amet, venenatis commodo integer tortor, lectus nibh maecenas</div>
<div class="abs timer" style="left:158px;top:2198px">10<small>Days</small></div>
<div class="abs timer" style="left:238px;top:2198px">8<small>Hours</small></div>
<div class="abs timer" style="left:318px;top:2198px">20<small>Min</small></div>
<div class="abs timer" style="left:398px;top:2198px">50<small>Sec</small></div>

<div class="abs" style="left:520px;top:1880px;width:160px;height:420px;border-radius:80px;background:#b8bde8"></div>
<div class="abs badge" style="top:1900px" role="img" aria-label="Line illustration of a boy's face"></div>
<div class="abs badge" style="top:2034px" role="img" aria-label="Line illustration of a mother and child"></div>
<div class="abs badge" style="top:2168px" role="img" aria-label="Line illustration of a toy robot"></div>
<div class="abs" style="left:730px;top:1945px;width:285px;height:330px;border-radius:40% 40% 10px 10px;background:linear-gradient(#f3d3c2,#8a4f38)" role="img" aria-label="Photo of a laughing baby holding a brown teddy bear"></div>

<div class="abs sec-title" style="left:0;top:2450px">LATEST FROM THE BLOG</div>

<div class="abs photo" style="left:170px;top:2550px;width:375px;height:252px;background:linear-gradient(120deg,#d9e6c9,#f2c8d6 60%,#e6b19a)" role="img" aria-label="Photo of a child with her mother in a supermarket"></div>
<div class="abs" style="left:325px;top:2660px;width:36px;height:36px;border-radius:4px;background:var(--pink)"></div>
<div class="abs" style="left:370px;top:2660px;width:36px;height:36px;border-radius:4px;background:var(--pink)"></div>
<div class="abs post-title" style="left:585px;top:2578px">KIDS ARE THE BEST EXPLORER</div>
<div class="abs post-text" style="left:585px;top:2615px">Lorem ipsum dolor sit amet, venenatis commodo integer tortor, lectus nibh maecenas leo rutrum ipsum tristique, ut mattis. Aliquam integer nam nulla taciti suspendisse, congue euismod consectetuer tellus rutrum, quisque non, duis blandit magna imperdiet</div>
<div class="abs post-meta" style="left:585px;top:2770px"><span class="more">Read more..</span><span>96Likes</span><span>Share</span><span>Show</span></div>

<div class="abs post-title" style="left:290px;top:2900px">CLOTH NEW QUALITY NOW</div>
<div class="abs post-text" style="left:200px;top:2937px;text-align:right">Lorem ipsum dolor sit amet, venenatis commodo integer tortor, lectus nibh maecenas leo rutrum ipsum tristique, ut mattis. Aliquam integer nam nulla taciti suspendisse, congue euismod consectetuer tellus rutrum, quisque non, duis blandit magna imperdiet</div>
<div class="abs post-meta" style="left:210px;top:3092px"><span>96Likes</span><span>Share</span><span>Show</span><span class="more">Read more..</span></div>
<div class="abs photo" style="left:655px;top:2865px;width:375px;height:255px;background:linear-gradient(120deg,#bcc9a9,#e9d5c4 50%,#6c86b8)" role="img" aria-label="Photo of parents choosing baby clothes in a shop"></div>

<div class="abs news"></div>
<div class="abs news-frame"></div>
<div class="abs head" style="left:300px;top:3278px;color:#fff;font-size:22px;font-style:italic;font-weight:700;letter-spacing:2px">NEWSLETTER</div>
<div class="abs" style="left:300px;top:3308px;color:#fff;font-size:11px;line-height:14px;width:250px">Cras lectus tellus mattis pulvinar,<br>mattis pulvinar.</div>
<div class="abs" style="left:600px;top:3293px;width:180px;height:40px;border-radius:20px;background:#f2efe6;font-size:12px;color:#bbb;line-height:40px;padding-left:20px">Your email..</div>
<div class="abs head" style="left:795px;top:3293px;width:100px;height:40px;border-radius:20px;background:var(--pink);color:#fff;font-size:13px;font-weight:700;letter-spacing:2px;line-height:40px;text-align:center">SEND</div>

<div class="abs footer"></div>

<div class="abs foot-h" style="left:110px;top:3538px">ABOUT US</div>
<div class="abs foot-list" style="left:110px;top:3573px;width:170px">Small kids shop with soft clothes, gentle toys and care for every new family day.</div>
<div class="abs" style="left:110px;top:3722px;display:flex;gap:14px">
  <span class="social"></span><span class="social"></span><span class="social"></span><span class="social"></span>
</div>

<div class="abs foot-h" style="left:358px;top:3538px">INFORMATION</div>
<ul class="abs foot-list" style="left:358px;top:3573px"><li>* Payment Policy</li><li>* Delivery Policy</li><li>* Return Products</li><li>* Refund Money</li><li>* Cookies</li></ul>

<div class="abs foot-h" style="left:615px;top:3538px">OUR SERVICES</div>
<ul class="abs foot-list" style="left:615px;top:3573px"><li>* Shipping delivery</li><li>* Tracking shipping</li><li>* Call center 24Hrs</li><li>* Secure payment</li><li>* Customer services</li></ul>

<div class="abs foot-h" style="left:872px;top:3538px">SHOP ADDRESS</div>
<ul class="abs foot-list" style="left:872px;top:3573px;line-height:24px"><li>12 Meadow Lane, Leeds</li><li>(+44) 0113 000 4821</li><li>(+44) 0113 000 7390</li><li>hello@pipandpod.example</li></ul>
<div class="abs" style="left:868px;top:3718px;display:flex;gap:14px">
  <span class="card-pay"></span><span class="card-pay"></span><span class="card-pay"></span><span class="card-pay"></span>
</div>

<div class="abs foot-bar">
  <span class="abs" style="left:125px;top:21px">Copyright 2017, all rights reserved, <span style="color:var(--sun)">Pip&amp;Pod</span></span>
  <span class="abs" style="left:770px;top:21px">Home &nbsp;|&nbsp; Shop &nbsp;|&nbsp; Delivery Information</span>
</div>

</body>
</html>
```